Create a promo image to demo to a restaurant the increase in $ they can achieve by using Verra

Create a promotional image to demonstrate to a restaurant the increase in revenue they can achieve by using Verra.

We have constructed the attached example of what we are looking for, open to alternatives however the main message is you will make more money from a Verra event than from your own restaurant for the same guests

We would like the restaurant image to look like the restaurant environment (show other tables in the background) and the same for the Customer dining room (plush private secure)

Please Verra branding where it fits best

Target Market(s)

Restaurants to signup

Industry/Entity Type

Restaurants and Catering

Requirements
Must have
• Simplicity and obviousness

```html
<!DOCTYPE html>
<html lang="en">
<head>
<meta charset="utf-8">
<title>Verra Dining – Get 3 Times More Revenue</title>
<link rel="stylesheet" href="https://fonts.googleapis.com/css2?family=Arimo:wght@400;700&display=swap">
<style>
  :root {
    --brand-purple: #7a2a82;
    --brand-mark: #8e2f8f;
    --accent-red: #e0312b;
    --ink: #111111;
    --paper: #ffffff;
    --tile-canapes: #2b8c8f;
    --tile-entree: #a8d8de;
    --tile-mains: #b04956;
    --tile-dessert: #e9b3b6;
    --tile-cocktail: #2f6f7d;
    --tile-cocktail-edge: #e07a2c;
  }
  * { margin: 0; padding: 0; box-sizing: border-box; }
  html, body { width: 1200px; height: 2316px; overflow: hidden; background: var(--paper); }
  body { font-family: "Arimo", Arial, sans-serif; color: var(--ink); }
  .canvas { position: relative; width: 1200px; height: 2316px; background: var(--paper); }

  .brand-square {
    position: absolute; left: 512px; top: 20px; width: 176px; height: 176px;
    background: var(--brand-mark); border-radius: 18px;
  }
  .brand-name {
    position: absolute; left: 0; right: 0; top: 196px; text-align: center;
    font-weight: 700; font-size: 92px; line-height: 1; color: var(--brand-purple);
    letter-spacing: -1px;
  }
  .tagline {
    position: absolute; left: 0; right: 0; top: 308px; text-align: center;
    font-weight: 700; font-size: 58px; line-height: 1; color: var(--accent-red);
  }
  .subline {
    position: absolute; left: 0; right: 0; top: 384px; text-align: center;
    font-size: 60px; line-height: 1;
  }
  .headline {
    position: absolute; left: 48px; right: 40px; top: 458px;
    font-weight: 700; font-size: 64px; line-height: 1.12;
  }
  .intro {
    position: absolute; left: 48px; right: 44px; top: 676px;
    font-size: 47px; line-height: 1.2;
  }

  .col-head { position: absolute; top: 928px; width: 420px; text-align: center; }
  .col-head--house { left: 30px; }
  .col-head--order { left: 720px; width: 420px; }
  .col-head h2 { font-weight: 700; font-size: 78px; line-height: 1; }
  .col-head p { font-size: 40px; line-height: 1.1; margin-top: 4px; }

  .course { position: absolute; left: 0; width: 1200px; height: 232px; }
  .course-label {
    position: absolute; left: 0; right: 0; top: 0; text-align: center;
    font-weight: 700; font-size: 44px; line-height: 1; color: var(--accent-red);
  }
  .course-tile {
    position: absolute; left: 524px; top: 58px; width: 152px; height: 152px;
  }
  .course-value {
    position: absolute; top: 100px; width: 420px; text-align: center;
    font-weight: 700; font-size: 72px; line-height: 1;
  }
  .course-value--house { left: 30px; }
  .course-value--order { left: 720px; }

  .tile--canapes { background: var(--tile-canapes); }
  .tile--entree { background: var(--tile-entree); }
  .tile--mains { background: var(--tile-mains); }
  .tile--dessert { background: var(--tile-dessert); }
  .tile--cocktail { background: var(--tile-cocktail); border: 8px solid var(--tile-cocktail-edge); }

  .total {
    position: absolute; top: 2232px; width: 420px; text-align: center;
    font-weight: 700; font-size: 80px; line-height: 1;
  }
  .total--house { left: 30px; }
  .total--order { left: 720px; }
</style>
</head>
<body>
<main class="canvas">
  <div class="brand-square" aria-hidden="true"></div>
  <h1 class="brand-name">Verra Dining</h1>
  <p class="tagline">Get 3 Times More Revenue</p>
  <p class="subline">Focus on home orders</p>
  <p class="headline">Your customer spends 3 times more on home orders</p>
  <p class="intro">We did the survey and the maths for you. Lets see the difference between an order for 8 guests inside a restaurant and the same people ordering in a customer's home</p>

  <div class="col-head col-head--house"><h2>In House</h2><p>Spending $</p></div>
  <div class="col-head col-head--order"><h2>Ordering</h2><p>Spending $</p></div>

  <section class="course" style="top:1064px">
    <span class="course-label">Canapes</span>
    <div class="course-tile tile--canapes" role="img" aria-label="Canapes plate icon"></div>
    <span class="course-value course-value--house">0 $</span>
    <span class="course-value course-value--order">128 $</span>
  </section>
  <section class="course" style="top:1296px">
    <span class="course-label">Entrée</span>
    <div class="course-tile tile--entree" role="img" aria-label="Entrée dish icon"></div>
    <span class="course-value course-value--house">100 $</span>
    <span class="course-value course-value--order">200 $</span>
  </section>
  <section class="course" style="top:1528px">
    <span class="course-label">Mains</span>
    <div class="course-tile tile--mains" role="img" aria-label="Main course icon"></div>
    <span class="course-value course-value--house">270 $</span>
    <span class="course-value course-value--order">360 $</span>
  </section>
  <section class="course" style="top:1760px">
    <span class="course-label">Dessert</span>
    <div class="course-tile tile--dessert" role="img" aria-label="Dessert slice icon"></div>
    <span class="course-value course-value--house">50 $</span>
    <span class="course-value course-value--order">200 $</span>
  </section>
  <section class="course" style="top:1992px">
    <span class="course-label">Cocktail</span>
    <div class="course-tile tile--cocktail" role="img" aria-label="Cocktail glass icon"></div>
    <span class="course-value course-value--house">50 $</span>
    <span class="course-value course-value--order">200 $</span>
  </section>

  <span class="total total--house">532 $</span>
  <span class="total total--order">1736 $</span>
</main>
</body>
</html>
```